Modern Business Card Design for Independent Urban Music Label

We need a card design for an independent urban music label called Copper Kite Records based in London. We develop and promote urban British music artists. We attend lots of high profile events with high profile industry people and want a card that comes across both on-brand and sophisticated, professional, trustworthy. I have attached our logo - please use the black and orange version in the upper left HOWEVER we are open to seeing other colors than the orange used though we want the shape of the logo to remain the same.

Info to please include:
Name
Position
Phone
Email
Website

Additional Info:
Twitter: @CopperKiteRecsUK
Insta: @CopperKiteRecs

Target Market(s)

Industry professionals and others artists

Industry/Entity Type

Business

Contact Information for Business Card

Info to please include:
Name
Position
Phone
Email
Website

Additional Info:
Twitter: @CopperKiteRecsUK
Insta: @CopperKiteRecs

Requirements
Must have
• Logo, company name
• Info to please include:
• Name
• Position
• Phone
• Email
• Website
Nice to have
• Twitter: @CopperKiteRecsUK
• Insta: @CopperKiteRecs
• If it can be done so that it doesn't look cluttered

```html
<!DOCTYPE html>
<html lang="en">
<head>
<meta charset="utf-8">
<title>Copper Kite Records – Business Card</title>
<link rel="stylesheet" href="https://fonts.googleapis.com/css2?family=Open+Sans:wght@400;600&family=Oswald:wght@500&display=swap">
<style>
  :root {
    --stage: #8c8c8c;
    --paper: #ffffff;
    --ink: #1b1b1d;
    --ink-deep: #0f0f11;
    --copper: #f0821e;
    --copper-deep: #e0621a;
    --text-light: #f2f2f2;
    --divider: #6b6b6b;
  }
  * { box-sizing: border-box; margin: 0; padding: 0; }
  html, body { width: 1200px; height: 900px; overflow: hidden; }
  body {
    background: var(--stage);
    display: flex;
    align-items: center;
    justify-content: center;
    gap: 40px;
    font-family: "Open Sans", sans-serif;
  }
  .card {
    width: 540px;
    height: 310px;
    border-radius: 22px;
    overflow: hidden;
    position: relative;
  }
  /* Front */
  .card--front { background: var(--paper); display: flex; flex-direction: column; }
  .front-brand {
    height: 168px;
    display: flex;
    align-items: flex-end;
    justify-content: center;
    padding-bottom: 22px;
  }
  .brand {
    display: flex;
    align-items: center;
    gap: 10px;
    font-family: "Oswald", sans-serif;
    font-weight: 500;
    color: var(--copper);
    letter-spacing: 0.06em;
    text-transform: uppercase;
  }
  .brand__dot { border-radius: 50%; background: var(--copper); flex: none; }
  .card--front .brand { font-size: 22px; }
  .card--front .brand__dot { width: 14px; height: 14px; }
  .front-stripe {
    height: 6px;
    background: linear-gradient(90deg, var(--copper), var(--copper-deep));
  }
  .front-info {
    flex: 1;
    background: linear-gradient(180deg, var(--ink), var(--ink-deep));
    display: flex;
    align-items: center;
    padding: 0 24px 0 30px;
  }
  .person { width: 180px; text-align: right; padding-right: 22px; align-self: flex-start; margin-top: 20px; }
  .person__name { color: var(--copper); font-size: 18px; font-weight: 400; }
  .person__role { color: var(--text-light); font-size: 12px; margin-top: 2px; }
  .info-divider { width: 1px; height: 92px; background: var(--divider); }
  .contacts { list-style: none; padding-left: 16px; color: var(--text-light); font-size: 14px; line-height: 19px; }
  .contacts li { display: flex; align-items: center; gap: 6px; }
  .contacts li.gap-before { margin-top: 9px; }
  .contacts svg { width: 14px; height: 14px; flex: none; }
  .social-square { width: 13px; height: 13px; background: var(--copper); border-radius: 2px; flex: none; }
  /* Back */
  .card--back {
    background: radial-gradient(ellipse at 60% 40%, #2a2a2d, var(--ink-deep) 75%);
    display: flex;
    align-items: center;
    justify-content: center;
  }
  .card--back .brand { font-size: 28px; }
  .card--back .brand__dot { width: 18px; height: 18px; }
</style>
</head>
<body>
  <section class="card card--front" aria-label="Business card front">
    <div class="front-brand">
      <div class="brand"><span class="brand__dot"></span><span>Copper Kite Records</span></div>
    </div>
    <div class="front-stripe"></div>
    <div class="front-info">
      <div class="person">
        <p class="person__name">Marcus Ellery</p>
        <p class="person__role">Manager</p>
      </div>
      <div class="info-divider"></div>
      <ul class="contacts">
        <li>
          <svg viewBox="0 0 16 16" aria-hidden="true"><path fill="#f0821e" d="M4 1.5l2.2 3-1.4 1.6c.8 1.9 2.3 3.4 4.2 4.3l1.6-1.4 3 2.1-1.2 2.6C6.8 13.6 2.3 9.1 1.5 3z"/></svg>
          <span>020 7946 0381</span>
        </li>
        <li>
          <svg viewBox="0 0 16 16" aria-hidden="true"><rect x="1" y="3" width="14" height="10" rx="1.5" fill="#f0821e"/><path d="M1.8 4l6.2 5 6.2-5" fill="none" stroke="#1b1b1d" stroke-width="1.3"/></svg>
          <span>info@copperkiterecords.com</span>
        </li>
        <li>
          <svg viewBox="0 0 16 16" aria-hidden="true"><g fill="none" stroke="#f0821e" stroke-width="1.4"><circle cx="8" cy="8" r="6.3"/><ellipse cx="8" cy="8" rx="2.8" ry="6.3"/><path d="M1.7 8h12.6M3 4.6h10M3 11.4h10"/></g></svg>
          <span>www.copperkiterecords.com</span>
        </li>
        <li class="gap-before"><span class="social-square"></span><span>@CopperKiteRecsUK</span></li>
        <li><span class="social-square"></span><span>@CopperKiteRecs</span></li>
      </ul>
    </div>
  </section>

  <section class="card card--back" aria-label="Business card back">
    <div class="brand"><span class="brand__dot"></span><span>Copper Kite Records</span></div>
  </section>
</body>
</html>
```